Maison Corvel

I am actually making my own traditional french food.
Everything is homemade with passion.
I make differente terrines, jams, macaroons, rillettes and much more
I do as well cocktail party and catering
Updates

Hello everyone,

On the business card I would like to see appear if it's possible these following informations: traditional french food, cocktail party and catering.

Industry/Entity Type

Catering

```html
<!DOCTYPE html>
<html lang="en">
<head>
<meta charset="utf-8">
<title>Maison Corvel – Business Card</title>
<link rel="stylesheet" href="https://fonts.googleapis.com/css2?family=Cinzel:wght@600;700&family=Marcellus+SC&family=Arimo&display=swap">
<style>
  :root {
    --backdrop: #7a5a3c;
    --card-white: #ffffff;
    --brand-red: #c0202f;
    --brand-blue: #2b2f8f;
    --ink: #1c1c1c;
    --on-red: #ffffff;
  }
  * { margin: 0; padding: 0; box-sizing: border-box; }
  html, body {
    width: 1101px;
    height: 1200px;
    overflow: hidden;
    background: var(--backdrop);
  }
  .canvas { position: relative; width: 1101px; height: 1200px; }
  .card { position: absolute; }
  .card-front {
    left: 106px; top: 69px;
    width: 881px; height: 503px;
    background: var(--card-white);
  }
  .card-back {
    left: 92px; top: 608px;
    width: 883px; height: 505px;
    background: var(--brand-red);
  }

  /* Wordmark with rules above and below */
  .wordmark {
    position: absolute;
    display: flex;
    flex-direction: column;
    align-items: center;
    font-family: "Cinzel", serif;
    font-weight: 700;
    text-transform: uppercase;
    white-space: nowrap;
  }
  .wordmark::before, .wordmark::after {
    content: "";
    display: block;
    width: 100%;
    background: currentColor;
  }
  .wordmark-front {
    left: 54px; top: 296px;
    width: 378px;
    color: var(--ink);
    font-size: 35px;
    letter-spacing: 1px;
  }
  .wordmark-front::before { height: 4px; margin-bottom: 6px; }
  .wordmark-front::after  { height: 4px; margin-top: 4px; }

  .abn-strip {
    position: absolute;
    left: 491px; top: 76px;
    width: 37px; height: 356px;
    background: var(--brand-blue);
  }
  .abn-number {
    position: absolute;
    left: 50%; top: 50%;
    transform: translate(-50%, -50%) rotate(-90deg);
    font-family: "Arimo", sans-serif;
    font-size: 20px;
    color: var(--on-red);
    white-space: nowrap;
  }
  .contact-panel {
    position: absolute;
    left: 536px; top: 76px;
    width: 345px; height: 356px;
    background: var(--brand-red);
    color: var(--on-red);
    padding: 113px 0 0 30px;
  }
  .contact-name {
    font-family: "Marcellus SC", serif;
    font-size: 25px;
    letter-spacing: 1px;
    margin-bottom: 24px;
  }
  .contact-line {
    display: flex;
    align-items: center;
    gap: 10px;
    font-family: "Arimo", sans-serif;
    font-size: 21px;
    margin-bottom: 14px;
  }
  .contact-line svg { width: 16px; height: 16px; flex: none; }

  .wordmark-back {
    left: 96px; top: 200px;
    width: 678px;
    color: var(--on-red);
    font-size: 68px;
    letter-spacing: 2px;
  }
  .wordmark-back::before { height: 5px; margin-bottom: 2px; }
  .wordmark-back::after  { height: 5px; margin-top: 0; }
  .services {
    position: absolute;
    left: 0; right: 0; top: 335px;
    text-align: center;
    font-family: "Marcellus SC", serif;
    font-size: 24px;
    letter-spacing: 2px;
    color: var(--on-red);
  }
</style>
</head>
<body>
<main class="canvas">
  <section class="card card-front">
    <p class="wordmark wordmark-front">Maison Corvel</p>
    <div class="abn-strip">
      <span class="abn-number">ABN:98712345610</span>
    </div>
    <div class="contact-panel">
      <p class="contact-name">Étienne Vasseur</p>
      <p class="contact-line">
        <svg viewBox="0 0 16 16" aria-hidden="true"><circle cx="8" cy="8" r="7" fill="none" stroke="currentColor" stroke-width="1.4"/><path d="M5.5 4.5l1.5 1.5-1 1.2c.6 1.3 1.5 2.2 2.8 2.8l1.2-1 1.5 1.5-1 1.2c-3-.5-5.6-3.1-6-6z" fill="currentColor"/></svg>
        0491836205
      </p>
      <p class="contact-line">
        <svg viewBox="0 0 16 16" aria-hidden="true"><rect x="1.5" y="4" width="13" height="9" fill="currentColor"/><path d="M1.5 4l6.5 5 6.5-5" fill="none" stroke="#c0202f" stroke-width="1.3"/></svg>
        etienne.v@corvel.fr
      </p>
    </div>
  </section>

  <section class="card card-back">
    <p class="wordmark wordmark-back">Maison Corvel</p>
    <p class="services">Traditional French food · Cocktail party &amp; Catering</p>
  </section>
</main>
</body>
</html>
```